braided hoses

Mr Colin Mayfair <colinmmayfair@quillnest.net>
Tue, Jun 25, 3:27 PM (17 hours ago)
to Priya

WE ARE LOOKING FOR A FLYER WE CAN EMAIL OU TO EXISTING CUSTOMERS - MECHANICAL INDUSTRIAL WHOLESALE ETC

WE SUPPLY PERFORMANCE FITTINGS TO MAKE BRAIDED HOSE FOR RACECAR, ENTHUSIASTS AND GENERAL CARS
these are used for
brake hoses
cooler lines
oil + fuel hoses

pictures supplied but if better pictures found will be ok
i do not want to pay for pictures afterwards

Requirements
Must have
• company details correct

```html
<!DOCTYPE html>
<html lang="en">
<head>
<meta charset="utf-8">
<title>Braided Hoses – Summit Motor Works</title>
<link rel="stylesheet" href="https://fonts.googleapis.com/css2?family=Poppins:wght@400;500;600&family=Russo+One&display=swap">
<style>
  :root{
    --yellow:#f7d417;
    --ink:#1d1e20;
    --dark:#26282b;
    --dark-2:#2e3034;
    --dark-3:#222427;
    --white:#ffffff;
    --photo-green:#4d6b3a;
    --photo-red:#c8141c;
    --product-bg:#eef0f2;
  }
  html,body{margin:0;padding:0;overflow:hidden;background:#fff;}
  .flyer{
    position:relative;width:848px;height:1200px;overflow:hidden;
    background:var(--white);font-family:"Poppins",sans-serif;color:var(--ink);
  }
  .hero-photo{
    position:absolute;left:0;top:0;width:848px;height:470px;
    background:
      linear-gradient(180deg,rgba(255,255,255,0) 55%,#fff 100%),
      radial-gradient(ellipse 45% 30% at 55% 55%,var(--photo-red) 0%,rgba(200,20,28,.85) 45%,rgba(200,20,28,0) 75%),
      linear-gradient(180deg,#3c5a2c 0%,var(--photo-green) 40%,#9aa3a0 62%,#d9dcdc 80%);
  }
  .brand-block{
    position:absolute;left:0;top:0;width:188px;height:135px;background:var(--yellow);
    display:flex;flex-direction:column;align-items:center;justify-content:center;gap:10px;
  }
  .brand-block .mark{width:30px;height:30px;background:var(--ink);}
  .brand-block .name{font-size:11.5px;font-weight:600;color:var(--ink);letter-spacing:.3px;}
  .headline{
    position:absolute;left:48px;top:466px;margin:0;
    font-family:"Russo One",sans-serif;font-weight:400;color:var(--ink);
    font-size:86px;line-height:80px;letter-spacing:2px;
    transform:skewX(-14deg) scaleX(1.32);transform-origin:left top;
  }
  .headline span{display:block;}
  .headline-rule{position:absolute;left:51px;top:627px;width:190px;height:4px;background:var(--yellow);}
  .intro{
    position:absolute;left:51px;top:657px;margin:0;width:520px;
    font-size:17.5px;font-weight:500;line-height:21px;color:var(--ink);
  }
  .dark-panel{position:absolute;left:0;top:0;width:848px;height:1200px;}
  .details{
    position:absolute;left:53px;top:841px;margin:0;width:620px;
    font-size:17.5px;line-height:22px;color:var(--white);font-weight:400;
  }
  .uses{position:absolute;left:52px;top:893px;margin:0;padding:0;list-style:none;}
  .uses li{
    display:flex;align-items:center;gap:9px;height:27px;
    font-size:18px;color:var(--white);
  }
  .uses svg{width:12px;height:11px;}
  .product{
    position:absolute;background:var(--white);border:1px solid var(--yellow);box-sizing:border-box;
  }
  .product .shot{position:absolute;inset:8px;}
  .product-set{left:527px;top:901px;width:270px;height:146px;}
  .product-set .shot{background:linear-gradient(120deg,#f4f5f6 0%,#d8dbe0 45%,#b7262c 60%,#2c4fb5 75%,#eef0f2 100%);}
  .product-elbow{left:408px;top:1003px;width:270px;height:145px;}
  .product-elbow .shot{background:radial-gradient(ellipse 30% 40% at 45% 50%,#c0202a 0%,#2c4fb5 55%,rgba(255,255,255,0) 80%),#fff;}
  .contacts{position:absolute;left:51px;top:1049px;margin:0;padding:0;list-style:none;}
  .contacts li{
    display:flex;align-items:center;gap:12px;height:36px;
    font-size:10px;color:var(--white);
  }
  .contacts svg{width:24px;height:24px;fill:none;stroke:var(--yellow);stroke-width:1.6;stroke-linecap:round;stroke-linejoin:round;}
</style>
</head>
<body>
<div class="flyer">
  <div class="hero-photo" role="img" aria-label="Red open-top sports car driving on a road past green hedges"></div>

  <div class="brand-block">
    <div class="mark"></div>
    <div class="name">SUMMIT MOTOR WORKS</div>
  </div>

  <h1 class="headline"><span>BRAIDED</span><span>HOSES</span></h1>
  <div class="headline-rule"></div>
  <p class="intro">Summit Motor Works can offer to have your hoses made in Braid for greater endurance and better look.</p>

  <svg class="dark-panel" viewBox="0 0 848 1200" aria-hidden="true">
    <polygon points="0,817 848,658 848,1200 0,1200" fill="var(--dark)"/>
    <polygon points="445,740 848,658 848,820 560,1200 300,1200" fill="var(--dark-2)"/>
    <polygon points="684,758 848,1010 848,1120 770,1063 600,900" fill="var(--dark-3)"/>
    <polygon points="684,758 520,1010 600,900" fill="var(--dark-2)"/>
    <polygon points="0,1000 260,1200 0,1200" fill="var(--dark-3)"/>
  </svg>

  <p class="details">We supply Performance Fittings to Make Braided Hose for Racecar, Enthusiasts and General Cars. These are used for:</p>
  <ul class="uses">
    <li><svg viewBox="0 0 12 11"><polygon points="6,1 11,10 1,10" fill="none" stroke="var(--yellow)" stroke-width="2"/></svg>brake hoses</li>
    <li><svg viewBox="0 0 12 11"><polygon points="6,1 11,10 1,10" fill="none" stroke="var(--yellow)" stroke-width="2"/></svg>cooler lines</li>
    <li><svg viewBox="0 0 12 11"><polygon points="6,1 11,10 1,10" fill="none" stroke="var(--yellow)" stroke-width="2"/></svg>oil + fuel hoses</li>
  </ul>

  <div class="product product-set"><div class="shot" role="img" aria-label="Assorted anodised red, blue and black braided hose fittings"></div></div>
  <div class="product product-elbow"><div class="shot" role="img" aria-label="Red and blue 90 degree braided hose end fitting"></div></div>

  <ul class="contacts">
    <li><svg viewBox="0 0 24 24"><path d="M5 3h4l2 5-2.5 1.5a11 11 0 0 0 6 6L16 13l5 2v4a2 2 0 0 1-2 2A16 16 0 0 1 3 5a2 2 0 0 1 2-2z"/></svg>0800 555 214</li>
    <li><svg viewBox="0 0 24 24"><rect x="2" y="5" width="20" height="14"/><path d="M2 5l10 8 10-8"/></svg>parts@summitmotorworks.co.nz</li>
    <li><svg viewBox="0 0 24 24"><circle cx="12" cy="12" r="10"/><path d="M2 12h20M12 2c3 3 3 17 0 20M12 2c-3 3-3 17 0 20M4 7h16M4 17h16"/></svg>summitmotorworks.co.nz</li>
  </ul>
</div>
</body>
</html>
```